Business card-Tales From The Harbor Gate

Looking for a business card. I have a website I designed "TalesFromTheHarborGate.com I am not a graphic artist and may at some point need help with my website too. Used the font "Hello Stockholm" on my website. I am a writer, looking to get published. Liked the "feel" of the cover below. No cliche typwriters, keyboards, pens. - Edgar P. Lindqvist
Updates

Not 100% sold on needing the owls, just a place to begin. I probably sounds like I'm going to be a pain to work with, I was a video production manager for 15+ years. When I would give an editor or graphic artist a project and let them run with it, the results were typically beyond my expectations. I give the idea then as the artists touch it, and adds value I could never bring to the project. Make something you would be proud of, don't try to second-guess me.

Target Market(s)

Agents, publishers, people I want to buy my book once I get it published

Industry/Entity Type

Publishing

Contact Information for Business Card

Edgar P. Lindqvist
TalesFromTheHarborGate.com
Phone #-TBD
Edgar@TalesFromTheHarbroGate.com
Maybe address; 418 N. 7th St Cheyenne, WY 82947

Colors
fcca95
3277b5

Requirements
Must have
• I like the "chromatic" feel of the attached cover. As you can see from my website, I'm an owl fan. Those pictures I took and do own the rights too. Not sure if they are approritae for a business card.
Should not have
• Cliche I like the "chromatic" feel of the attached book cover.
• I will need help with my website at some point too. I want the website to be easy for me to update, and reflect the same feel as the card. I write adventure, mystery. I have romance in my books too...Adventure of Romance, Romance of adventure, I am not sure but those words were like by an author firned of mine. They are rather "light" reading too.

```html
<!DOCTYPE html>
<html lang="en">
<head>
<meta charset="utf-8">
<title>Tales From The Harbor Gate – Business Card</title>
<link rel="stylesheet" href="https://fonts.googleapis.com/css2?family=Roboto:wght@300;400;500&display=swap">
<style>
  :root {
    --stage-top: #46474b;
    --stage-bottom: #161618;
    --card-black: #0b0a0a;
    --wordmark: #dcdcdc;
    --gold: #b8953f;
    --muted: #8a8783;
    --contact: #9a9793;
    --icon: #c9c6c2;
  }
  * { box-sizing: border-box; margin: 0; padding: 0; }
  html, body { width: 680px; height: 1200px; overflow: hidden; }
  body {
    background: linear-gradient(180deg, var(--stage-top) 0%, var(--stage-bottom) 100%);
    font-family: "Roboto", Arial, sans-serif;
    position: relative;
  }
  .card {
    position: absolute;
    width: 600px;
    height: 358px;
    background: var(--card-black);
    overflow: hidden;
    box-shadow: 0 18px 40px rgba(0,0,0,.55), 0 4px 10px rgba(0,0,0,.4);
  }
  .card--front { left: 24px; top: 170px; }
  .card--back  { left: 56px; top: 660px; }

  /* Front */
  .front-photo {
    position: absolute;
    left: 170px; top: -40px;
    width: 460px; height: 440px;
    background:
      radial-gradient(ellipse 42% 46% at 42% 42%, rgba(215,206,194,.95) 0%, rgba(150,128,108,.85) 35%, rgba(92,62,44,.7) 60%, rgba(11,10,10,0) 100%),
      radial-gradient(ellipse 30% 40% at 78% 45%, rgba(90,58,40,.9) 0%, rgba(11,10,10,0) 100%);
  }
  .wordmark {
    position: absolute;
    left: 62px; top: 168px;
    width: 260px;
    text-align: right;
    color: var(--wordmark);
    font-weight: 400;
    font-size: 27px;
    line-height: 1.25;
  }

  /* Back */
  .back-photo {
    position: absolute;
    right: 0; top: 0;
    width: 300px; height: 358px;
    background:
      radial-gradient(ellipse 32% 22% at 45% 42%, rgba(205,160,40,.9) 0%, rgba(205,160,40,0) 100%),
      radial-gradient(ellipse 60% 55% at 55% 55%, rgba(150,128,90,.95) 0%, rgba(90,78,55,.8) 45%, rgba(11,10,10,0) 100%);
    -webkit-mask-image: linear-gradient(90deg, transparent 0%, #000 22%);
            mask-image: linear-gradient(90deg, transparent 0%, #000 22%);
  }
  .identity { position: absolute; left: 67px; top: 64px; }
  .identity__name {
    color: var(--gold);
    font-size: 30px;
    font-weight: 400;
    letter-spacing: .2px;
  }
  .identity__role {
    color: var(--muted);
    font-size: 15px;
    margin-top: 4px;
    letter-spacing: .5px;
  }
  .contact-list {
    position: absolute;
    left: 67px; top: 180px;
    list-style: none;
    color: var(--contact);
    font-size: 16px;
  }
  .contact-list li {
    display: flex;
    align-items: flex-start;
    gap: 10px;
    line-height: 21px;
    margin-bottom: 10px;
  }
  .contact-list li.address { margin-top: -10px; }
  .contact-list svg { flex: 0 0 13px; width: 13px; height: 13px; margin-top: 4px; fill: var(--icon); }
</style>
</head>
<body>

<section class="card card--front" aria-label="Card front">
  <div class="front-photo" role="img" aria-label="Photograph of a great horned owl perched on a person's arm, in a soft vignette"></div>
  <div class="wordmark">Tales From The<br>Harbor Gate</div>
</section>

<section class="card card--back" aria-label="Card back">
  <div class="back-photo" role="img" aria-label="Close-up photograph of a great horned owl's head and golden eye"></div>
  <div class="identity">
    <h1 class="identity__name">Edgar P. Lindqvist</h1>
    <p class="identity__role">CEO</p>
  </div>
  <ul class="contact-list">
    <li>
      <svg viewBox="0 0 16 16" aria-hidden="true"><path d="M3.5 1.5l2.5 0 1 3.5-1.6 1.2a9 9 0 0 0 4.4 4.4L11 9l3.5 1v2.5c0 1-1 2-2 2A11 11 0 0 1 1.5 3.5c0-1 1-2 2-2z"/></svg>
      <span>TBD</span>
    </li>
    <li>
      <svg viewBox="0 0 16 16" aria-hidden="true"><path d="M1 3.5h14v9H1z M1.8 4.3L8 9l6.2-4.7" fill="none" stroke="#c9c6c2" stroke-width="1.4"/></svg>
      <span>Edgar@TalesFromTheHarbroGate.com</span>
    </li>
    <li>
      <svg viewBox="0 0 16 16" aria-hidden="true"><g fill="none" stroke="#c9c6c2" stroke-width="1.3"><circle cx="8" cy="8" r="6.5"/><ellipse cx="8" cy="8" rx="2.8" ry="6.5"/><path d="M1.5 8h13M2.5 4.8h11M2.5 11.2h11"/></g></svg>
      <span>TalesFromTheHarborGate.com</span>
    </li>
    <li class="address">
      <svg viewBox="0 0 16 16" aria-hidden="true"><path d="M8 1a5 5 0 0 1 5 5c0 3.6-5 9-5 9S3 9.6 3 6a5 5 0 0 1 5-5zm0 3a2 2 0 1 0 0 4 2 2 0 0 0 0-4z"/></svg>
      <span>418 N. 7th St Cheyenne,<br>WY 82947</span>
    </li>
  </ul>
</section>

</body>
</html>
```